Website Design for Videographer

I am looking to update my website - www.lukebranwell.com. I am a wedding videographer who specialises in natural and documentary videography.

The website will be built by my designer using the Wordpress Brightform framework.

Requirements;
I want the website to have a clean white look mixed in with video footage.
Needs to be classy. At the moment my website uses a lot of Gold. On the new look I DO NOT want gold.

Need a web and mobile design for the following 12 pages;

* Home page (need to have example videos and text)
* About (this is about me and my service)
* Videos (examples of my work)
* Testimonials
* Packages
* Contact
* Content (this is to show social media content that I am making in a vertical format and advertise this service).
* Blog (index page for blog)
* Blog pages (individual pages for blog content)
* Wedding Venues Index Page (https://lukebranwell.com/north-east-wedding-venues/)
* Individual venue pages (https://lukebranwell.com/north-east-wedding-venues/holmfield-lodge-wedding-videos/) - Needs to show videos, photos, text as is on the current page.
* Venue Tours (https://lukebranwell.com/wedding-venue-tours/)

My current logo is attached however on the website I want to go for a black and white style for it.

Example styles I like however must not be copied.
https://joelmarrick.co.uk/about/
https://stoneandfern.co.uk/ (if done in white)
https://bouncyplumreels.co.uk/

Target Market(s)

Couples getting married aged 25-35

Industry/Entity Type

Weddings

Number of Pages Required

5+ page

Font styles to use
Sans Serif

Requirements
Must have
• A classy look, black and white, use videos and photos.
Should not have
• Gold colour

```html
<!DOCTYPE html>
<html lang="en">
<head>
<meta charset="utf-8">
<title>Luke Branwell — North East Wedding Videographer</title>
<link href="https://fonts.googleapis.com/css2?family=Newsreader:ital,opsz,wght@0,6..72,300;1,6..72,300&family=Inter:wght@400;500;600&display=swap" rel="stylesheet">
<style>
:root{
  --backdrop:#2a2a29;
  --cream:#f7f6f1;
  --white:#ffffff;
  --ink:#222220;
  --muted:#5b5a55;
  --rule:#d6d4cc;
  --forest:#26331f;
  --night:#1c1c1a;
  --photo-green:linear-gradient(165deg,#2f3a22 0%,#55633a 35%,#3c4a2a 60%,#7a8458 100%);
  --photo-dusk:linear-gradient(165deg,#1f211b 0%,#3f3d2e 40%,#55513c 65%,#24251e 100%);
  --photo-day:linear-gradient(180deg,#a9bdd0 0%,#b49e7a 38%,#7a6848 62%,#556237 100%);
  --photo-warm:linear-gradient(160deg,#8d7a66 0%,#4c4235 55%,#d9d4c8 100%);
}
*{margin:0;padding:0;box-sizing:border-box}
html,body{width:1200px;height:5245px;overflow:hidden;background:var(--backdrop)}
body{font-family:"Inter",sans-serif;color:var(--ink)}
.display{font-family:"Newsreader",serif;font-weight:300;font-optical-sizing:auto}
.page{position:absolute;left:145px;top:145px;width:910px;height:4958px;background:var(--white);overflow:hidden}
.abs{position:absolute}
.photo{position:absolute;background:var(--photo-green)}
.photo.dusk{background:var(--photo-dusk)}
.photo.day{background:var(--photo-day)}
.photo.warm{background:var(--photo-warm)}
.body-copy{font-size:12.5px;line-height:1.6;color:var(--muted)}
.link-under{font-size:12px;color:var(--muted);border-bottom:1px solid var(--muted);padding-bottom:3px}
em{font-style:italic}

/* nav */
.nav{top:0;left:0;width:910px;height:85px;background:var(--cream)}
.nav a{position:absolute;top:30px;font-size:8.5px;color:var(--muted);text-decoration:none}
.brand{position:absolute;left:395px;top:27px;width:120px;text-align:center;font-family:"Newsreader",serif;font-weight:300;font-size:14px;color:var(--ink)}
.nav .enquire{border-bottom:1px solid var(--rule);width:56px;padding-bottom:4px}
.menu{position:absolute;left:833px;top:31px;width:12px;height:6px;border-top:2px solid var(--ink);border-bottom:2px solid var(--ink)}

/* hero */
.hero{top:85px;left:0;width:910px;height:452px;background:var(--cream)}
.hero-title{position:absolute;left:45px;top:112px;width:818px;text-align:center;color:var(--cream);font-size:96px;line-height:90px;letter-spacing:1px}
.hero-copy{position:absolute;left:300px;top:310px;width:310px;text-align:center;color:#f1efe8;font-size:12.5px;line-height:1.6}
.hero-cta{position:absolute;left:400px;top:380px;width:110px;text-align:center;color:#e8e6df;font-size:9px;border-bottom:1px solid #e8e6df;padding-bottom:4px;opacity:.6}

/* films intro */
.intro-title{left:63px;top:600px;font-size:46px;line-height:46px}
.thumbs{left:438px;top:859px;width:410px;display:flex;justify-content:space-between}
.thumbs span{display:block;width:71px;height:45px;background:var(--photo-green)}

/* offering */
.offering{top:973px;left:0;width:910px;height:677px;background:var(--cream)}
.eyebrow{font-size:9px;font-weight:600;letter-spacing:.5px;color:var(--ink)}
.offer-list{position:absolute;left:0;top:105px;width:910px;text-align:center;font-size:100px;line-height:100px;color:var(--ink)}

/* together */
.together-title{left:63px;top:2104px;font-size:46px;line-height:46px}

/* dark collage */
.dark{top:2267px;left:0;width:910px;height:527px;background:var(--night)}
.dark-title{position:absolute;left:190px;top:118px;width:530px;text-align:center;color:var(--cream);font-size:44px;line-height:44px}
.dark-copy{position:absolute;left:270px;top:292px;width:370px;text-align:center;color:#e7e5de;font-size:12.5px;line-height:1.6}
.pill-light{position:absolute;left:335px;top:354px;width:240px;height:38px;border-radius:20px;background:var(--cream);color:var(--ink);font-family:"Newsreader",serif;font-size:13px;text-align:center;line-height:38px}

/* featured */
.featured{top:2794px;left:0;width:910px;height:514px;background:var(--cream)}
.feat-title{left:63px;top:120px;font-size:60px;line-height:58px}
.feat-list{position:absolute;left:63px;top:250px;width:342px}
.feat-list li{list-style:none;display:flex;justify-content:space-between;align-items:center;height:43px;border-top:1px solid var(--rule);font-family:"Newsreader",serif;font-weight:300;font-size:15px;color:var(--muted)}
.feat-list li:first-child{border-top:none}
.feat-list li span{font-family:"Inter",sans-serif;font-size:9px}

/* experience */
.experience{top:3308px;left:0;width:910px;height:472px;background:var(--photo-dusk)}
.exp-panel{position:absolute;left:0;top:0;width:370px;height:472px;background:var(--forest)}
.exp-title{position:absolute;left:8px;top:62px;white-space:nowrap;color:var(--cream);font-size:86px;line-height:1}
.exp-copy{position:absolute;left:60px;top:210px;width:250px;text-align:center;color:#dcdcd0;font-family:"Newsreader",serif;font-weight:300;font-size:15px;line-height:1.7}
.pill-outline{position:absolute;left:63px;top:363px;width:240px;height:38px;border-radius:20px;border:1px solid #dcdcd0;color:#dcdcd0;font-family:"Newsreader",serif;font-size:13px;text-align:center;line-height:36px}

/* explore */
.post-title{font-family:"Newsreader",serif;font-weight:300;font-size:22px;line-height:1.25;color:var(--ink);width:370px}

/* footer */
.foot-badge{left:63px;top:4378px;display:flex;align-items:center;gap:8px;font-family:"Newsreader",serif;font-weight:300;font-size:15px}
.foot-badge i{display:block;width:26px;height:26px;border-radius:50%;border:1px solid var(--ink)}
.foot-links{position:absolute;font-family:"Newsreader",serif;font-weight:300;font-size:22px;line-height:46px;color:var(--muted)}
.social-title{left:0;top:4552px;white-space:nowrap;font-size:92px;line-height:1;color:#4a4a47}
.strip{left:0;top:4674px;width:910px;height:284px;display:flex}
.strip span{flex:1;background:var(--photo-green)}
</style>
</head>
<body>
<div class="page">

  <header class="abs nav">
    <a style="left:63px">About Luke</a>
    <a style="left:135px">Wedding films</a>
    <a style="left:205px">Testimonials</a>
    <div class="brand">Luke Branwell</div>
    <a style="left:609px">Packages</a>
    <a style="left:680px">Blog</a>
    <a class="enquire" style="left:752px">Enquire</a>
    <span class="menu"></span>
  </header>

  <section class="abs hero">
    <div class="photo" role="img" aria-label="Bride and groom walking together across a garden lawn in front of an ivy-covered manor" style="left:45px;top:0;width:818px;height:440px;background:linear-gradient(180deg,#3a3f2a 0%,#5a6440 30%,#44502d 55%,#6e7a4a 78%,#8d9264 100%)"></div>
    <h1 class="display hero-title">LUKE<br>BRANWELL</h1>
    <p class="hero-copy">A trusted and acclaimed North East wedding videographer who has more than 25 years of videography experience.</p>
    <span class="hero-cta">Watch films</span>
  </section>

  <h2 class="abs display intro-title">Stunning<br><em>wedding films</em><br>in <em>the</em> North East</h2>
  <p class="abs body-copy" style="left:63px;top:767px;width:300px">If you're looking for a highly experienced wedding videographer who focuses on your story, the "goosebump" moments and the emotions, then get in touch with Luke today.</p>
  <span class="abs link-under" style="left:63px;top:870px">Watch films</span>
  <div class="photo" role="img" aria-label="Groom and bride holding hands on the lawn outside a lit country venue" style="left:438px;top:595px;width:410px;height:246px;background:linear-gradient(180deg,#2e3325 0%,#4d5236 35%,#5f7240 65%,#889560 100%)"></div>
  <div class="abs thumbs">
    <span role="img" aria-label="Wedding film still, couple portrait"></span>
    <span role="img" aria-label="Wedding film still, bride in gown" style="background:var(--photo-dusk)"></span>
    <span role="img" aria-label="Wedding film still, garden ceremony"></span>
    <span role="img" aria-label="Wedding film still, venue exterior" style="background:var(--photo-day)"></span>
    <span role="img" aria-label="Wedding film still, couple on terrace"></span>
  </div>

  <section class="abs offering">
    <div class="abs eyebrow" style="left:0;width:910px;text-align:center;top:76px">MY OFFERING</div>
    <div class="photo warm" role="img" aria-label="Bride smiling while holding her bouquet" style="left:611px;top:222px;width:100px;height:133px"></div>
    <div class="photo warm" role="img" aria-label="Guests gathered during a wedding ceremony" style="left:0;top:412px;width:200px;height:110px;background:linear-gradient(100deg,#9a8b78,#5a5044 40%,#3a342c 70%,#6b6358)"></div>
    <div class="display offer-list">VIDEO<br>IMAGES<br>EDITORIAL<br>SUPPORT</div>
    <p class="abs body-copy" style="left:270px;top:534px;width:370px;text-align:center">When you look back on your wedding day, I want you to remember the genuine smiles, genuine laughing, and spontaneous moments of emotion that you might have missed in the flurry of events.</p>
  </section>

  <div class="photo" role="img" aria-label="Bride and groom standing on a lawn beside an ivy-covered building" style="left:63px;top:1717px;width:238px;height:356px;background:linear-gradient(180deg,#4a4a34 0%,#3d4a2a 45%,#5b6b3a 75%,#7d8a55 100%)"></div>
  <div class="photo dusk" role="img" aria-label="Groom and bride embracing on a tree-lined path" style="left:336px;top:1717px;width:238px;height:356px"></div>
  <div class="photo day" role="img" aria-label="Couple sitting on a stone balustrade before a gothic manor house" style="left:609px;top:1717px;width:238px;height:356px"></div>
  <h2 class="abs display together-title"><em>let's do it</em><br>TOGETHER</h2>
  <p class="abs body-copy" style="left:574px;top:2140px;width:272px">I understand that on the best day of your life everything has to be perfect and you need time to make a decision.</p>

  <section class="abs dark">
    <div class="photo" role="img" aria-label="Bride by a tall window" style="left:0;top:14px;width:170px;height:318px;background:linear-gradient(160deg,#6e625a,#2e2a25)"></div>
    <div class="photo dusk" role="img" aria-label="Evening garden scene at the venue" style="left:190px;top:14px;width:530px;height:318px"></div>
    <div class="photo" role="img" aria-label="Manor house rooftops in golden light" style="left:740px;top:14px;width:170px;height:318px;background:linear-gradient(170deg,#3e4a55,#7a6a4f)"></div>
    <div class="photo" role="img" aria-label="Guests celebrating" style="left:0;top:352px;width:112px;height:166px;background:linear-gradient(160deg,#55607a,#3b3a33)"></div>
    <div class="photo dusk" role="img" aria-label="Couple walking at dusk" style="left:130px;top:352px;width:310px;height:166px"></div>
    <div class="photo" role="img" aria-label="Bride's gown detail" style="left:460px;top:352px;width:310px;height:166px;background:linear-gradient(160deg,#2a2925,#6a655b)"></div>
    <div class="photo dusk" role="img" aria-label="Trees at the venue" style="left:790px;top:352px;width:120px;height:166px"></div>
    <h2 class="dark-title display"><em>the</em><br>MOST IMPORTANT DAY<br>OF YOUR LIFE</h2>
    <p class="dark-copy">Your wedding film is the best way to keep this day alive forever… a newlywed's gift that keeps giving an infinite reminder of those special moments and memories.</p>
    <span class="pill-light">Watch more</span>
  </section>

  <section class="abs featured">
    <h2 class="abs display feat-title"><em>featured</em><br>VIDEOS</h2>
    <ul class="feat-list">
      <li>Ashcombe Hall Wedding<span>View more</span></li>
      <li>Durham Celebration<span>View more</span></li>
      <li>Holmfield Lodge Love<span>View more</span></li>
    </ul>
    <div class="photo" role="img" aria-label="Wedding party seated in an ornate hall, bridesmaids in sage dresses" style="left:438px;top:125px;width:410px;height:270px;background:linear-gradient(180deg,#2b2220 0%,#4a3a34 35%,#7d9c8a 60%,#c9c5b8 80%,#2a2628 100%)"></div>
  </section>

  <section class="abs experience" role="img" aria-label="Garden steps and a white rotunda at a wedding venue">
    <div class="exp-panel"></div>
    <div class="photo" role="img" aria-label="Bride and groom holding hands on a lawn" style="left:438px;top:138px;width:410px;height:204px;background:linear-gradient(180deg,#3e4a2c,#6f7f4b 60%,#b8b8a8)"></div>
    <h2 class="exp-title display">ON <em>my</em> EXPERIENCE</h2>
    <p class="exp-copy">Watch Sophie talking <em>about</em> how having Luke Branwell as her Wedding Videographer was <em>one of the</em> best services at her wedding.</p>
    <span class="pill-outline">Watch more</span>
  </section>

  <div class="abs eyebrow" style="left:63px;top:3853px">MORE TO EXPLORE</div>
  <div class="photo" role="img" aria-label="Ruined abbey among green trees and lawn" style="left:63px;top:3884px;width:375px;height:245px;background:linear-gradient(180deg,#b9cde0 0%,#6f8a4c 35%,#8e8c6a 60%,#6c7a40 100%)"></div>
  <div class="photo" role="img" aria-label="Bride and groom sharing a close, laughing moment" style="left:472px;top:3884px;width:375px;height:245px;background:linear-gradient(160deg,#2a2a28,#6b6a63 55%,#c7c2b8)"></div>
  <h3 class="abs post-title" style="left:63px;top:4157px">What's The Role Of A Best Man At A Wedding?</h3>
  <h3 class="abs post-title" style="left:472px;top:4157px">What Does It Mean To Have A Wedding Venue All To Yourself?</h3>
  <span class="abs link-under" style="left:63px;top:4225px">Read more</span>
  <span class="abs link-under" style="left:472px;top:4225px">Read more</span>

  <div class="abs foot-badge"><i></i>Luke Branwell</div>
  <p class="abs body-copy" style="left:63px;top:4452px;width:270px;font-size:12px;line-height:1.5;color:var(--ink)">A trusted and acclaimed North East wedding videographer who has more than 25 years of videography experience.</p>
  <div class="foot-links" style="left:550px;top:4380px">About Luke<br>Wedding Films<br>Testimonials</div>
  <div class="foot-links" style="left:754px;top:4380px">Packages<br>Blog<br>Enquire</div>

  <h2 class="abs display social-title">FIND ME ON CLIPWAVE /</h2>
  <div class="abs strip">
    <span role="img" aria-label="White garden rotunda among trees"></span>
    <span role="img" aria-label="Couple walking outside a country hotel" style="background:var(--photo-day)"></span>
    <span role="img" aria-label="Gothic manor house with stone terrace" style="background:linear-gradient(180deg,#7d9bb8,#7c6a4c 60%,#4f5a35)"></span>
    <span role="img" aria-label="Bride holding a bouquet under a veil" style="background:linear-gradient(160deg,#3a4a2c,#c9c6bd)"></span>
  </div>

</div>
</body>
</html>
```